Rack card for a integrative medical practice

Need an eye-catching rack card with our logo with content as provided. We have a membership based holistic medical practice which incorporates western and holistic medicine. We would like to focus on wellness and healthy lifestyle. See uploaded files for what is included in the membership. Would like 2 page rack card color on both sides. Logo must be on the front.

Target Market(s)

People looking for alternative medicine, healthy lifestyle.

Industry/Entity Type

Health and Wellness

Colors
00AB8E
00BBA5
67D7C9
C6EFE9
E9F9F6

Requirements
Must have
• Must spark interest at first sight. Clear message.
Nice to have
• Warm, bright and positive vibe. Organic, neutral and earthy colors.
Should not have
• Traditional medical practice vibe (cold, formal, industrial). No PINK except the logo.

```html
<!DOCTYPE html>
<html lang="en">
<head>
<meta charset="utf-8">
<title>Lilara Health &amp; Wellness – Rack Card</title>
<link rel="stylesheet" href="https://fonts.googleapis.com/css2?family=Oswald:wght@300;400;500&display=swap">
<style>
  :root {
    --teal-deep: #00AB8E;
    --teal: #00BBA5;
    --teal-mid: #67D7C9;
    --teal-soft: #C6EFE9;
    --teal-mist: #E9F9F6;
    --sand: #f3efe7;
    --ink: #1c2624;
    --page: #ffffff;
  }
  * { box-sizing: border-box; margin: 0; padding: 0; }
  html, body { width: 1200px; height: 1057px; overflow: hidden; background: var(--page); }
  body { position: relative; font-family: "Oswald", sans-serif; color: var(--ink); }

  .card { position: absolute; width: 543px; height: 852px; background: var(--teal-deep); overflow: hidden; }
  .card__inner { position: absolute; inset: 0; overflow: hidden; }

  /* Front */
  .card--front { left: 59px; top: 148px; z-index: 2; }
  .card--front .card__inner {
    background: linear-gradient(180deg, var(--sand) 0%, var(--teal-mist) 45%, var(--teal-soft) 100%);
    border-top-left-radius: 110px 220px;
    border-bottom-right-radius: 90px 170px;
  }
  .front__photo {
    position: absolute; left: 0; top: 0; width: 100%; height: 290px;
    background: linear-gradient(180deg, #d7dcd6 0%, #cfd8d2 40%, #e4ede8 80%, var(--teal-mist) 100%);
  }
  .front__glow {
    position: absolute; left: 40px; bottom: 40px; width: 420px; height: 360px;
    border-radius: 50%;
    background: radial-gradient(ellipse at center, rgba(103,215,201,0.40) 0%, rgba(198,239,233,0) 70%);
  }
  .front__name {
    position: absolute; top: 300px; width: 100%; text-align: center;
    font-weight: 300; font-size: 92px; line-height: 1; color: var(--teal-deep); letter-spacing: 1px;
  }
  .front__sub {
    position: absolute; top: 412px; width: 100%; text-align: center;
    font-weight: 300; font-size: 57px; line-height: 1;
  }
  .rule { position: absolute; height: 2px; background: var(--teal-deep); opacity: 0.85; }
  .front__rule { left: 65px; width: 400px; }
  .front__tagline {
    position: absolute; top: 548px; width: 100%; text-align: center;
    font-weight: 400; font-size: 36px; line-height: 56px;
  }
  .accent { color: var(--teal-deep); }
  .front__address {
    position: absolute; top: 786px; width: 100%; text-align: center;
    font-weight: 300; font-size: 29px; line-height: 1;
  }

  /* Back */
  .card--back { left: 595px; top: 54px; z-index: 1; }
  .card--back .card__inner {
    background: linear-gradient(180deg, var(--sand) 0%, var(--teal-mist) 55%, var(--teal-soft) 100%);
    border-top-right-radius: 110px 200px;
    border-bottom-left-radius: 70px 130px;
  }
  .back__photo {
    position: absolute; left: 0; bottom: 0; width: 100%; height: 140px;
    background: linear-gradient(180deg, rgba(198,239,233,0) 0%, #b4e6de 60%, #9fdcd2 100%);
  }
  .brand {
    position: absolute; top: 92px; width: 100%; text-align: center;
    font-weight: 400; font-size: 46px; letter-spacing: 8px; line-height: 1; color: var(--ink);
  }
  .back__rule { left: 90px; width: 370px; }
  .back__heading {
    position: absolute; top: 182px; width: 100%; text-align: center;
    font-weight: 400; font-size: 38px; line-height: 56px;
  }
  .benefits { position: absolute; top: 318px; left: 14px; width: 512px; list-style: none; }
  .benefits li {
    position: relative; padding-left: 14px;
    font-weight: 300; font-size: 29px; line-height: 38.5px;
  }
  .benefits li::before {
    content: ""; position: absolute; left: 0; top: 15px;
    border-left: 6px solid var(--teal-deep); border-top: 5px solid transparent; border-bottom: 5px solid transparent;
  }
</style>
</head>
<body>

  <section class="card card--back" aria-label="Rack card back">
    <div class="card__inner">
      <div class="back__photo" role="img" aria-label="Soft-focus photo of an acupuncture treatment"></div>
      <div class="brand">LILARA</div>
      <div class="rule back__rule" style="top:174px"></div>
      <h2 class="back__heading">What’s Included in Your<br>MEMBERSHIP :</h2>
      <div class="rule back__rule" style="top:303px"></div>
      <ul class="benefits">
        <li>Unlimited office visits with no copay</li>
        <li>Direct communication with your doctor</li>
        <li>Discounted labs, imaging and medications</li>
        <li>Free initial acupuncture session (<span class="accent">$250 value</span>).</li>
        <li>2 BodyScan testings per year (<span class="accent">$100 value</span>)</li>
        <li>Discounts for supplements and health products in the clinic</li>
        <li>Discounts for iv vitamin infusion therapy</li>
        <li>Personalized nutrition plan after advanced testing such as gut microbiome, hormonal, metabolism test, etc.</li>
      </ul>
    </div>
  </section>

  <section class="card card--front" aria-label="Rack card front">
    <div class="card__inner">
      <div class="front__photo" role="img" aria-label="Photo of a person meditating beside candles, a reed diffuser and stacked stones"></div>
      <div class="front__glow" role="img" aria-label="Faint lotus petals in the background"></div>
      <h1 class="front__name">LILARA</h1>
      <p class="front__sub">Health &amp; Wellness</p>
      <div class="rule front__rule" style="top:541px"></div>
      <p class="front__tagline">A Direct<br>Primary Care Practice<br>Focused on a More <span class="accent">HOLISTIC</span></p>
      <div class="rule front__rule" style="top:728px"></div>
      <p class="front__address">2140 N Elm St., STE 4B Riverton</p>
    </div>
  </section>

</body>
</html>
```